Varnel Group Limited Stationary

We are in need of business card and letterhead designs. We are looking for clean modern designs that complement the style and feel of our logo.

Industry/Entity Type

Business

```html
<!DOCTYPE html>
<html lang="en">
<head>
<meta charset="utf-8">
<title>Varnel Group Limited – Business Card</title>
<link href="https://fonts.googleapis.com/css2?family=Montserrat:wght@700&family=Questrial&display=swap" rel="stylesheet">
<style>
  :root{
    --backdrop:#4b4b4b;
    --card-white:#f4f4f4;
    --brand-blue:#0f3c8c;
    --brand-navy:#0a2f78;
    --mark-dark:#2e3440;
    --text-grey:#555a60;
    --faint-grey:#d2d2d2;
    --rule-grey:#b9b9b9;
    --white:#ffffff;
  }
  *{margin:0;padding:0;box-sizing:border-box}
  html,body{width:1200px;height:1000px;overflow:hidden}
  body{background:var(--backdrop);position:relative;font-family:"Questrial",sans-serif}
  .card{position:absolute;width:528px;height:301px;border-radius:14px;overflow:hidden}
  .card-front{left:207px;top:164px;background:var(--card-white)}
  .card-back{left:474px;top:551px;background:linear-gradient(180deg,var(--brand-navy),#143f8f 60%,#0c3380)}
  .holder-name{position:absolute;left:35px;top:61px;font-family:"Montserrat",sans-serif;font-weight:700;font-size:20px;color:var(--brand-blue);letter-spacing:.2px}
  .holder-role{position:absolute;left:35px;top:86px;font-size:14.5px;color:var(--text-grey)}
  .brand{position:absolute;left:248px;top:52px;display:flex;align-items:center;gap:12px}
  .brand-dot{width:48px;height:48px;border-radius:50%;background:var(--brand-blue)}
  .brand-name{font-size:22px;color:var(--brand-blue);letter-spacing:1px}
  .faint-circle{position:absolute;left:408px;top:186px;width:136px;height:136px;border-radius:50%;background:var(--faint-grey)}
  .contact{position:absolute;left:35px;top:246px;display:flex;font-size:11.5px;color:var(--text-grey);line-height:16px}
  .contact-col{padding:0 8px;border-left:1px solid var(--rule-grey)}
  .contact-col:first-child{padding-left:0;border-left:none}
  .contact-row{display:flex;align-items:center;gap:6px}
  .contact-row svg{width:11px;height:11px;flex:none}
  .back-name{position:absolute;left:29px;top:128px;font-size:28px;color:var(--white);letter-spacing:1.5px}
  .back-rule{position:absolute;left:29px;top:165px;width:220px;height:1px;background:linear-gradient(90deg,rgba(255,255,255,.1),rgba(255,255,255,.8),rgba(255,255,255,.1))}
  .back-circle{position:absolute;left:294px;top:24px;width:260px;height:260px;border-radius:50%;background:var(--mark-dark)}
</style>
</head>
<body>
  <section class="card card-front">
    <div class="holder-name">MILES CORRAN</div>
    <div class="holder-role">Managing Director</div>
    <div class="brand">
      <div class="brand-dot"></div>
      <div class="brand-name">Varnel Group</div>
    </div>
    <div class="faint-circle"></div>
    <div class="contact">
      <div class="contact-col">
        <div class="contact-row"><svg viewBox="0 0 11 11"><rect width="11" height="11" rx="2" fill="var(--brand-blue)"/><rect x="3.5" y="2" width="4" height="7" rx="1" fill="#fff"/></svg>(07) 5120 4417</div>
        <div class="contact-row"><svg viewBox="0 0 11 11"><rect width="11" height="11" rx="2" fill="var(--brand-blue)"/><rect x="2.5" y="4" width="6" height="4" fill="#fff"/><rect x="3.5" y="2" width="4" height="2" fill="#fff"/></svg>(07) 5120 4490</div>
      </div>
      <div class="contact-col">
        <div class="contact-row"><svg viewBox="0 0 11 11"><rect width="11" height="11" rx="2" fill="var(--brand-blue)"/><rect x="2" y="3" width="7" height="5" fill="#fff"/><path d="M2 3l3.5 3L9 3" stroke="var(--brand-blue)" fill="none"/></svg>info@varnelgroup.com</div>
        <div class="contact-row"><svg viewBox="0 0 11 11"><rect width="11" height="11" rx="2" fill="var(--brand-blue)"/><circle cx="5.5" cy="5.5" r="3.2" fill="none" stroke="#fff"/><path d="M2.3 5.5h6.4M5.5 2.3v6.4" stroke="#fff" stroke-width=".7"/></svg>www.varnelgroup.com</div>
      </div>
      <div class="contact-col">
        <div>Suite 4, 87B</div>
        <div>Marlow Bay QLD</div>
      </div>
    </div>
  </section>

  <section class="card card-back">
    <div class="back-name">Varnel Group</div>
    <div class="back-rule"></div>
    <div class="back-circle"></div>
  </section>
</body>
</html>
```